Präsentationsvorlagen für Automotive Engineering
Zielgruppe
Automotive Engineering - Software & Embedded systems are main focus including V-Modell
Aufgabenstellung
see Logo

```html
<!DOCTYPE html>
<html lang="de">
<head>
<meta charset="utf-8">
<title>KARVION Präsentationsvorlage</title>
<link rel="stylesheet" href="https://fonts.googleapis.com/css2?family=Arimo:wght@400;700&family=Open+Sans:wght@400;600&display=swap">
<style>
:root{
  --navy:#0b2f63;
  --red:#f6222f;
  --paper:#ffffff;
  --mist:#eef1f6;
  --ink:#3a4a63;
  --rule:#d5dae3;
}
*{box-sizing:border-box;margin:0;padding:0}
html,body{width:1200px;height:4383px;overflow:hidden;background:#fff}
body{position:relative;font-family:"Open Sans",Arial,sans-serif;color:var(--ink)}
.slide{position:absolute;width:783px;height:442px;background:var(--paper);box-shadow:0 2px 8px rgba(0,0,0,.18);overflow:hidden}
.slide *{position:absolute}
.tab{left:0;top:20px;width:22px;height:135px;background:var(--navy);border-radius:0 22px 22px 0}
.foot{left:17px;top:418px;font:700 12px "Arimo",Arial,sans-serif;color:var(--navy);letter-spacing:2px;white-space:nowrap}
.foot span{font-weight:400;letter-spacing:0;padding-left:4px;border-left:1px solid var(--navy);margin-left:4px}
.h-red{font:700 38px/1.15 "Arimo",Arial,sans-serif;color:var(--red)}
.small{font-size:9px;line-height:1.75;color:var(--ink)}
.photo{display:block}
.bullet{display:flex;align-items:center;gap:22px;font-size:9px;white-space:nowrap;position:absolute}
.bullet i{position:static;width:15px;height:15px;border-radius:50%;background:var(--navy);display:block}
.bullet i svg{position:static;display:block}

/* cover */
.cover{background:var(--navy)}
.cover .panel{left:123px;top:92px;width:660px;height:258px;background:var(--mist)}
.cover .name{left:123px;top:180px;width:660px;text-align:center;font:700 66px "Arimo",Arial,sans-serif;color:var(--navy);letter-spacing:10px}
.cover .dot{left:638px;top:200px;width:16px;height:16px;background:var(--red)}

/* toc */
.toc h2{left:77px;top:50px;font:700 30px "Arimo",Arial,sans-serif;color:var(--navy)}
.toc .item{width:140px}
.toc .item h3{position:static;font:700 14px "Arimo",Arial,sans-serif;color:var(--red)}
.toc .item p{position:static;font-size:8.5px;line-height:1.9;margin-top:2px;height:34px}
.toc .item b{position:static;display:block;font:700 26px "Arimo",Arial,sans-serif;color:var(--navy);margin-top:8px}

/* vorwort */
.quote .bubble{left:287px;top:100px;width:226px;height:226px;border-radius:50% 50% 50% 50%/48% 48% 52% 52%;background:var(--red)}
.quote .qmark{left:380px;top:130px;font:700 36px "Arimo",Arial,sans-serif;color:#fff}
.quote .qtext{left:305px;top:183px;width:190px;text-align:center;font:600 17px/1.35 "Arimo",Arial,sans-serif;color:#fff}
.quote .ring{left:350px;top:298px;width:100px;height:100px;border:1.5px dashed var(--navy);border-radius:50%}
.quote .avatar{left:363px;top:311px;width:74px;height:74px;border-radius:50%;background:radial-gradient(circle at 50% 40%,#b78462,#5b3d2c)}
.quote .who{left:568px;top:284px;font:700 15px "Arimo",Arial,sans-serif;color:var(--navy)}
.quote .role{left:568px;top:304px;font-size:8px}
</style>
</head>
<body>

<!-- 1 Cover -->
<section class="slide cover" style="left:178px;top:80px">
  <div class="panel"></div>
  <div class="name">KARVION</div>
</section>

<!-- 2 Inhaltsverzeichnis -->
<section class="slide toc" style="left:178px;top:608px">
  <div class="tab"></div>
  <h2>INHALTVERZEICHNIS</h2>
  <div class="item" style="left:80px;top:130px"><h3>Über uns</h3><p>Lorem ipsum dolor sit<br>amet dolor</p><b>01</b></div>
  <div class="item" style="left:238px;top:130px"><h3>Lorem ipsum</h3><p>Ipsum lorem dolor sit</p><b>02</b></div>
  <div class="item" style="left:397px;top:130px"><h3>Team</h3><p>Ispum lorem dolor, sit<br>lorem dolor amet</p><b>03</b></div>
  <div class="item" style="left:80px;top:282px"><h3>Services</h3><p>Lorem ipsum sit amet</p><b>04</b></div>
  <div class="item" style="left:238px;top:282px"><h3>Lorem ipsum</h3><p>Lorem ipsum dolor sit<br>amet dolor</p><b>05</b></div>
  <div class="item" style="left:397px;top:282px"><h3>Kontakt</h3><p>Amet dolor, sit amet dolor<br>lorem ipse</p><b>06</b></div>
  <div class="photo" role="img" aria-label="Nahaufnahme eines Getriebes mit Zahnrädern" style="left:550px;top:45px;width:233px;height:350px;background:linear-gradient(135deg,#2c4fb8,#7d9ad6 45%,#c3ccd8 70%,#1d3b8f)"></div>
  <div class="foot">KARVION</div>
</section>

<!-- 3 Vorwort -->
<section class="slide quote" style="left:178px;top:1135px">
  <div class="tab"></div>
  <div class="bubble"></div>
  <div class="qmark">“</div>
  <div class="qtext">Lorem ipsum dolor sit amet. Dolor lorem amet sit ipse.</div>
  <div class="ring"></div>
  <div class="avatar" role="img" aria-label="Porträtfoto des Geschäftsführers"></div>
  <div class="h-red" style="left:568px;top:170px">Vorwort</div>
  <div class="small" style="left:568px;top:216px;width:170px;font-size:8px">Lorem ipsum dolor sit amet dolor lorem ipsum sit amet.</div>
  <div class="who">Jonas Beispiel</div>
  <div class="role">Geschäftsführer</div>
  <div class="foot">KARVION</div>
</section>

<!-- 4 Text mit Bild -->
<section class="slide" style="left:178px;top:1662px">
  <div class="tab"></div>
  <div class="photo" role="img" aria-label="Ingenieure im Labor an einem Prüfstand" style="left:68px;top:45px;width:350px;height:275px;background:linear-gradient(120deg,#1c2840,#5d6f8c 45%,#a9b6c7 60%,#26344e)"></div>
  <div class="h-red" style="left:458px;top:45px">Lorem ipsum,<br>dolor sit amet.</div>
  <div class="small" style="left:460px;top:170px;width:270px;font-size:8.5px">Cras maximus fermentum ipsum, id auctor magna maximus a. Lorem ipsum dolor sit amet, consectetur adipiscing elit. Donec dictum enim at diam rhoncus, et facilisis nulla accumsan. Vestibulum maximus id est quis rutrum.</div>
  <div class="small" style="left:460px;top:262px;width:270px;font-size:8.5px">Cras maximus fermentum ipsum, id auctor magna maximus a. Lorem ipsum dolor sit amet, consectetur adipiscing elit. Donec dictum enim at diam rhoncus, et facilisis nulla accumsan. Vestibulum maximus id est quis rutrum.</div>
  <div class="foot">KARVION<span>3</span></div>
</section>

<!-- 5 Über uns -->
<section class="slide" style="left:178px;top:2188px">
  <div class="tab"></div>
  <svg width="783" height="442" style="left:0;top:0" role="img" aria-label="Softwareentwickler arbeiten am Computer">
    <defs><linearGradient id="teamGrad" x1="0" y1="0" x2="1" y2="1"><stop offset="0" stop-color="#e9ecef"/><stop offset=".55" stop-color="#b98c7a"/><stop offset="1" stop-color="#c0202b"/></linearGradient></defs>
    <polygon points="493,0 783,0 783,442 397,442" fill="url(#teamGrad)"/>
  </svg>
  <div class="h-red" style="left:78px;top:45px">Über uns</div>
  <div class="small" style="left:80px;top:117px;width:290px;font-size:8.5px">Duis vitae velit dignissim, consequat nisi id, accumsan nunc. Vestibulum nec diam diam. In hac habitasse platea dictumst. Phasellus neque urna, varius sit amet nisi sit amet, vulputate feugiat mauris.</div>
  <div class="bullet" style="left:80px;top:204px"><i><svg width="15" height="15" viewBox="0 0 15 15"><path d="M4 7.5h6M7.5 5l2.5 2.5L7.5 10" stroke="#fff" stroke-width="1.4" fill="none"/></svg></i>Praesent id sollicitudin diam</div>
  <div class="bullet" style="left:80px;top:237px"><i><svg width="15" height="15" viewBox="0 0 15 15"><path d="M4 7.5h6M7.5 5l2.5 2.5L7.5 10" stroke="#fff" stroke-width="1.4" fill="none"/></svg></i>Nulla porta nulla nisl, non aliquet tellus</div>
  <div class="bullet" style="left:80px;top:269px"><i><svg width="15" height="15" viewBox="0 0 15 15"><path d="M4 7.5h6M7.5 5l2.5 2.5L7.5 10" stroke="#fff" stroke-width="1.4" fill="none"/></svg></i>Donec non finibus dui</div>
  <div class="bullet" style="left:80px;top:302px"><i><svg width="15" height="15" viewBox="0 0 15 15"><path d="M4 7.5h6M7.5 5l2.5 2.5L7.5 10" stroke="#fff" stroke-width="1.4" fill="none"/></svg></i>Suspendisse sodales sit amet ligula at gravida</div>
  <div class="foot">KARVION<span>4</span></div>
</section>

<!-- 6 V-Modell -->
<section class="slide" style="left:178px;top:2717px">
  <div class="photo" role="img" aria-label="Hochhausfassade mit Lichtspuren" style="left:0;top:0;width:135px;height:442px;background:linear-gradient(160deg,#0f2a55,#5f7ea6 50%,#203e6b)"></div>
  <div class="h-red" style="left:135px;top:40px;width:648px;text-align:center">V-Modell</div>
  <svg width="783" height="442" style="left:0;top:0" font-family="Open Sans, Arial, sans-serif">
    <g fill="none" stroke="#0b2f63" stroke-width="1"><rect x="265" y="112" width="95" height="20"/><rect x="543" y="112" width="97" height="20"/></g>
    <g font-size="8.5" fill="#0b2f63" text-anchor="middle">
      <text x="312" y="125">Auftragnehmer</text><text x="591" y="125">Auftraggeber</text>
      <text x="453" y="125" font-weight="600" letter-spacing="1">Validierungs- und</text>
      <text x="453" y="135" font-weight="600" letter-spacing="1">Testbasis</text>
    </g>
    <g fill="#0b2f63">
      <polygon points="250,153 380,153 372,203 258,203"/>
      <polygon points="518,153 648,153 640,203 526,203"/>
      <polygon points="265,222 393,222 385,272 273,272"/>
      <polygon points="502,222 630,222 622,272 510,272"/>
      <polygon points="283,288 410,288 402,338 291,338"/>
      <polygon points="485,288 612,288 604,338 493,338"/>
      <polygon points="302,358 430,358 422,408 310,408"/>
      <polygon points="465,358 595,358 587,408 473,408"/>
    </g>
    <g font-size="8.5" fill="#fff" text-anchor="middle">
      <text x="315" y="175">Anforderungs-</text><text x="315" y="186">spezifikation</text>
      <text x="583" y="181">Abnahmetest</text>
      <text x="329" y="244">Systementwurf-</text><text x="329" y="255">funktional</text>
      <text x="566" y="250">Systemtest</text>
      <text x="346" y="310">Systementwurf-</text><text x="346" y="321">technisch</text>
      <text x="548" y="316">Integrationstest</text>
      <text x="366" y="380">Modul-</text><text x="366" y="391">spezifikation</text>
      <text x="530" y="386">Modultest</text>
    </g>
    <g stroke="#0b2f63" stroke-width="1.5" fill="#0b2f63">
      <line x1="390" y1="178" x2="508" y2="178"/><path d="M384 178l8-4v8zM514 178l-8-4v8z" stroke="none"/>
      <line x1="403" y1="247" x2="492" y2="247"/><path d="M397 247l8-4v8zM498 247l-8-4v8z" stroke="none"/>
      <line x1="420" y1="313" x2="475" y2="313"/><path d="M414 313l8-4v8zM481 313l-8-4v8z" stroke="none"/>
      <line x1="440" y1="383" x2="455" y2="383"/><path d="M434 383l8-4v8zM461 383l-8-4v8z" stroke="none"/>
    </g>
  </svg>
  <div class="foot" style="left:680px;top:418px"><span style="border:none;border-right:1px solid var(--navy);padding:0 4px 0 0;margin:0 4px 0 0">15</span>KARVION</div>
</section>

<!-- 7 Anforderungsspezifikation -->
<section class="slide" style="left:178px;top:3243px">
  <div class="photo" role="img" aria-label="Hand zeigt auf Programmcode am Bildschirm" style="left:0;top:0;width:218px;height:307px;background:linear-gradient(150deg,#1b2233,#4a5a74 45%,#d9c3b3 75%,#eef0f3)"></div>
  <div class="bullet" style="left:275px;top:41px"><i><svg width="15" height="15" viewBox="0 0 15 15"><path d="M4 7.5h6M7.5 5l2.5 2.5L7.5 10" stroke="#fff" stroke-width="1.4" fill="none"/></svg></i>Nulla porta nulla nisl, non aliquet</div>
  <div class="bullet" style="left:275px;top:74px"><i><svg width="15" height="15" viewBox="0 0 15 15"><path d="M4 7.5h6M7.5 5l2.5 2.5L7.5 10" stroke="#fff" stroke-width="1.4" fill="none"/></svg></i>Lorem ipsum dolor site amet</div>
  <div class="bullet" style="left:275px;top:107px"><i><svg width="15" height="15" viewBox="0 0 15 15"><path d="M4 7.5h6M7.5 5l2.5 2.5L7.5 10" stroke="#fff" stroke-width="1.4" fill="none"/></svg></i>Duis vitae velit dignissim</div>
  <div class="bullet" style="left:527px;top:41px"><i><svg width="15" height="15" viewBox="0 0 15 15"><path d="M4 7.5h6M7.5 5l2.5 2.5L7.5 10" stroke="#fff" stroke-width="1.4" fill="none"/></svg></i>Lorem ipsum dolor sit amet</div>
  <div class="bullet" style="left:527px;top:74px"><i><svg width="15" height="15" viewBox="0 0 15 15"><path d="M4 7.5h6M7.5 5l2.5 2.5L7.5 10" stroke="#fff" stroke-width="1.4" fill="none"/></svg></i>Vestibulum nec diam diam in hac</div>
  <div class="bullet" style="left:527px;top:107px"><i><svg width="15" height="15" viewBox="0 0 15 15"><path d="M4 7.5h6M7.5 5l2.5 2.5L7.5 10" stroke="#fff" stroke-width="1.4" fill="none"/></svg></i>Varius sit amet nisi sit amet, vulputate</div>
  <div style="left:142px;top:170px;width:641px;height:272px;background:var(--navy)"></div>
  <div style="left:192px;top:240px;font:700 26px 'Arimo',Arial,sans-serif;color:var(--red)">Anforderungsspezifikation</div>
  <div class="small" style="left:192px;top:288px;width:480px;font-size:8.5px;color:#fff">Duis vitae velit dignissim, consequat nisi id, accumsan nunc. Vestibulum nec diam diam. In hac habitasse platea dictumst. Phasellus neque urna, varius sit amet nisi sit amet, vulputate feugiat mauris. Cras molestie convallis condimentum. Vivamus libero eros, blandit nec dui at, iaculis viverra neque. Nam ultricies neque quis dui ultrices sagittis sed ac orci. Praesent id sollicitudin diam. Morbi at ornare lectus. Praesent blandit ante id ex imperdiet congue. Sed eget placerat lorem, semper varius ex.</div>
  <div class="foot">KARVION<span>16</span></div>
</section>

<!-- 8 Kontakt -->
<section class="slide" style="left:213px;top:3772px">
  <div class="tab"></div>
  <div class="h-red" style="left:78px;top:45px">Kontakt</div>
  <div class="small" style="left:82px;top:103px;width:290px;font-size:8.5px">Vestibulum nec diam diam. In hac habitasse platea dictumst. Phasellus neque urna, varius sit amet nisi sit amet, vulputate feugiat mauris. Cras molestie convallis condimentum.</div>
  <div style="left:82px;top:187px;font:700 15px 'Arimo',Arial,sans-serif;color:var(--navy)">Tel</div>
  <div class="small" style="left:205px;top:190px">+49 123 4567 890</div>
  <div style="left:82px;top:222px;width:258px;height:1px;background:var(--rule)"></div>
  <div style="left:82px;top:250px;font:700 15px 'Arimo',Arial,sans-serif;color:var(--navy)">E-Mail</div>
  <div class="small" style="left:205px;top:253px">info@karvion.de</div>
  <div style="left:82px;top:288px;width:258px;height:1px;background:var(--rule)"></div>
  <div style="left:82px;top:320px;font:700 15px 'Arimo',Arial,sans-serif;color:var(--navy)">Adresse</div>
  <div class="small" style="left:205px;top:318px;line-height:1.6">12345 Irgendwo,<br>Musterstr 9.</div>
  <div style="left:82px;top:362px;width:258px;height:1px;background:var(--rule)"></div>
  <div style="left:82px;top:393px;font:700 15px 'Arimo',Arial,sans-serif;color:var(--navy)">Web</div>
  <div class="small" style="left:205px;top:396px">www.karvion.de</div>
  <div style="left:598px;top:75px;width:167px;height:167px;background:var(--red)"></div>
  <div style="left:465px;top:122px;width:270px;height:263px;background:#fff;border:1px solid var(--navy)"></div>
  <div style="left:465px;top:232px;width:270px;text-align:center;font:700 40px 'Arimo',Arial,sans-serif;color:var(--navy);letter-spacing:5px">KARVION</div>
</section>

</body>
</html>
```